Logo + Business Card Design Project

We are looking at changing our logo and reprinting business cards.

Attached is a design concept for the logo (we have no hi res files for this).

The logo needs to be able to work standalone without the tagline.

We are happy for you to use this concept or design a new one. The existing concept is quite well liked.

We would also consider not having Solutions in the logo and just have QRV Systems Pty Ltd in the body text of the card.

We have a Tag Line that needs to go on all documentation / websites etc wherever the logo appears.

Tagline: Raising the bar

Our message to clients is that we have solutions that:

QRV Systems:
Raising the bar

Turning up Revenue
Turning up Profit
Turning up Confidence

We would require the files in a High Res format for print and a scalable transparent format for web.
(We also need greyscale and monochrome files)
All source files need to be delivered with existing layers etc

A corporate guide with the logo usage and colours should be specified.

Suggestions:
The new logo has to have CMYK colours of 100 90 0 0

CMYK 100 90 0 0
RGB #21409A
Websafe #224499
Greyscale #414141

We would also need a business card layout designed.
Could be one sided or 2 sided. Will probably print matt cello 2 sides on 350gsm gloss
Updates

Industry/Entity Type

Business

Requirements
Should not have
• Lower case n in QRV.

```html
<!DOCTYPE html>
<html lang="en">
<head>
<meta charset="utf-8">
<title>QRV Systems – Business Card</title>
<link rel="stylesheet" href="https://fonts.googleapis.com/css2?family=Montserrat:wght@400;600;700&display=swap">
<style>
  :root {
    --brand-blue: #21409a;
    --ink: #414141;
    --soft-grey: #8a8a8a;
    --ghost-grey: #efefef;
    --rule-grey: #c9c9c9;
    --card-white: #ffffff;
    --backdrop: #e6e6e6;
  }
  * { box-sizing: border-box; margin: 0; padding: 0; }
  html, body { width: 849px; height: 1200px; overflow: hidden; }
  body {
    background: var(--backdrop);
    font-family: "Montserrat", Arial, sans-serif;
    color: var(--ink);
    position: relative;
  }
  .card {
    position: absolute;
    left: 74px;
    width: 700px;
    height: 400px;
    background: var(--card-white);
    overflow: hidden;
    box-shadow: 0 4px 14px rgba(0,0,0,0.15);
  }
  .card--front { top: 160px; }
  .card--back { top: 640px; }

  /* Front */
  .company-name {
    position: absolute; left: 48px; top: 60px;
    display: flex; align-items: center; gap: 14px;
    font-weight: 700; font-size: 56px; line-height: 1;
    color: var(--brand-blue);
  }
  .company-name__dot {
    width: 18px; height: 18px; border-radius: 50%;
    background: var(--brand-blue);
  }
  .tagline {
    position: absolute; left: 200px; top: 198px;
    font-weight: 600; font-size: 30px; line-height: 1; color: var(--ink);
  }
  .promise {
    position: absolute; left: 540px; top: 190px;
    font-weight: 600; font-size: 12px;
    line-height: 1.45; color: var(--brand-blue); letter-spacing: 1px;
  }
  .swoosh { position: absolute; left: 0; bottom: 0; }

  /* Back */
  .ghost-name {
    position: absolute; left: 0; right: 0; top: 40px; text-align: center;
    font-weight: 700; font-size: 110px; line-height: 1;
    color: var(--ghost-grey);
  }
  .holder { position: absolute; right: 48px; top: 200px; text-align: right; }
  .holder__name { font-weight: 600; font-size: 20px; color: var(--brand-blue); }
  .holder__role { font-size: 14px; color: var(--soft-grey); margin-top: 2px; }
  .contact {
    position: absolute; top: 262px;
    display: grid; grid-template-columns: 70px auto; row-gap: 6px;
    font-size: 12px; padding-left: 14px;
    border-left: 1px solid var(--rule-grey);
  }
  .contact--phones { left: 40px; }
  .contact--online { left: 340px; }
  .contact dt { color: var(--soft-grey); }
  .contact dd { color: var(--ink); }
  .card-rule {
    position: absolute; left: 40px; right: 40px; top: 248px;
    height: 1px; background: var(--rule-grey);
  }
</style>
</head>
<body>

<section class="card card--front" aria-label="Business card front">
  <div class="company-name"><span>QRV Systems</span><span class="company-name__dot"></span></div>
  <p class="tagline">Raising the bar</p>
  <p class="promise">GROWTH<br>MARGIN<br>AND TRUST</p>
  <svg class="swoosh" width="700" height="400" viewBox="0 0 700 400" aria-hidden="true">
    <path d="M0,292 C220,340 470,330 700,272 L700,400 L0,400 Z" fill="var(--brand-blue)"/>
    <path d="M0,280 C220,326 470,318 700,260" fill="none" stroke="var(--brand-blue)" stroke-width="2"/>
  </svg>
</section>

<section class="card card--back" aria-label="Business card back">
  <div class="ghost-name" aria-hidden="true">QRV Systems</div>
  <div class="holder">
    <p class="holder__name">Daniel Corrigan</p>
    <p class="holder__role">Project Director</p>
  </div>
  <div class="card-rule"></div>
  <dl class="contact contact--phones">
    <dt>Phone</dt><dd>+61 2 9000 1100</dd>
    <dt>Support</dt><dd>+61 2 9000 1122</dd>
    <dt>Fax</dt><dd>+61 2 9000 1101</dd>
    <dt>Mobile</dt><dd>0400 555 019</dd>
  </dl>
  <dl class="contact contact--online">
    <dt>Email</dt><dd>daniel.corrigan@qrvsystems.com.au</dd>
    <dt>Web</dt><dd>www.qrvsystems.com.au</dd>
    <dt>Address</dt><dd>18/42 Harbour Lane<br>Northmead NSW 2152</dd>
  </dl>
</section>

</body>
</html>
```